Basic / Quick Business Card

Quick easy design project!

Need a one sided basic business card that matches font & style of brand and bottle label for our gourmet condiment, Velvet Marlow Sauce. Velvet Marlow Sauce is sold in specialty retail, gourmet groceries and appears on chef-driven restaurant menus, so the target market is a high end, gourmet, artisan-made food-loving customer.

Files Included:
Sauce Bottle Label
Velvet Marlow Sauce Round Logos

**About the logos - the logo may be used in a circle or alone vertically as on side of the bottle label**

Layout of Card:
May be vertical or horizontal based on designer ideas.

Logo usage (in circle vs. stand alone vertical logo) is up to designers descretion as well.

Reverse side of business card will be various high end / professional product photos / food shots using us.prindex.com system. **Designer on this project will NOT design a reserve for the card.**

Paper that will be used for printing:
Prindex Basic - it's a WHITE paper, but we use a cream background on Velvet Marlow Sauce branding, so please take this into account on design to stay brand consistent.

Elements & Copy for Card:
1. Logo in either script horizontal or vertical version
2. Copy: "Artisan Made - Small Batch"
3. Name - Glen Worsley
4. Title - Creator
5. Phone - xxx.xxx.xxxx
6. xxxx@velvetmarlow.com
7. URL: velvetmarlowsauce.com
8. Social Media: @getvelvetmarlow on Chirpline / Friendwall / Snapgrid

Please provide final files in Illustrator or InDesign format.

```html
<!DOCTYPE html>
<html lang="en">
<head>
<meta charset="utf-8">
<title>Velvet Marlow Sauce – Business Card</title>
<link rel="stylesheet" href="https://fonts.googleapis.com/css2?family=Courier+Prime:wght@400;700&family=Nothing+You+Could+Do&display=swap">
<style>
  :root {
    --backdrop: #e9e6e6;
    --ink: #1d1a17;
    --mustard: #e6a11a;
    --cream: #efeedd;
  }
  * { box-sizing: border-box; margin: 0; padding: 0; }
  html, body { width: 1200px; height: 867px; overflow: hidden; }
  body {
    background: var(--backdrop);
    font-family: "Courier Prime", "Courier New", monospace;
    color: var(--ink);
    position: relative;
  }
  .card {
    position: absolute;
    left: 75px; top: 133px;
    width: 1050px; height: 600px;
    background: var(--ink);
    padding: 9px;
  }
  .card__band {
    width: 100%; height: 100%;
    background: var(--mustard);
    padding: 14px;
  }
  .card__inner-rule {
    width: 100%; height: 100%;
    background: var(--ink);
    padding: 15px;
  }
  .card__face {
    position: relative;
    width: 100%; height: 100%;
    background: var(--cream);
  }
  .dash-frame {
    position: absolute;
    left: 20px; top: 34px; right: 22px; bottom: 34px;
    border: 3px dashed var(--mustard);
  }
  .tagline {
    position: absolute;
    top: 20px; right: 46px;
    padding: 0 8px;
    background: var(--cream);
    font-weight: 700;
    font-size: 22px;
    letter-spacing: 0.5px;
    line-height: 28px;
  }
  .brand-name {
    position: absolute;
    left: 100px; top: 168px;
    width: 260px;
    font-weight: 700;
    font-size: 48px;
    line-height: 52px;
    text-align: center;
    color: var(--ink);
  }
  .contact {
    position: absolute;
    left: 508px; top: 178px;
  }
  .contact__name {
    font-family: "Nothing You Could Do", cursive;
    font-size: 40px;
    line-height: 48px;
  }
  .contact__title {
    font-weight: 700;
    font-size: 22px;
    line-height: 28px;
    margin-bottom: 36px;
  }
  .contact__line {
    font-weight: 700;
    font-size: 22px;
    line-height: 34px;
    white-space: nowrap;
  }
  .social {
    position: absolute;
    left: 46px; right: 46px; top: 442px;
    display: flex;
    justify-content: space-between;
    align-items: center;
  }
  .social__item {
    display: flex;
    align-items: center;
    gap: 12px;
    font-weight: 700;
    font-size: 22px;
  }
  .social__mark {
    width: 22px; height: 22px;
    border-radius: 3px;
    background: var(--mustard);
  }
</style>
</head>
<body>
  <div class="card">
    <div class="card__band">
      <div class="card__inner-rule">
        <div class="card__face">
          <div class="dash-frame"></div>
          <div class="tagline">Artisan Made - Small Batch</div>

          <div class="brand-name">Velvet<br>Marlow<br>Sauce</div>

          <div class="contact">
            <div class="contact__name">Glen Worsley</div>
            <div class="contact__title">Creator</div>
            <div class="contact__line">P. 123.456.7890</div>
            <div class="contact__line">E. worsley@velvetmarlow.com</div>
            <div class="contact__line">W.www.velvetmarlowsauce.com</div>
          </div>

          <div class="social">
            <div class="social__item" aria-label="Chirpline"><span class="social__mark"></span>@getvelvetmarlow</div>
            <div class="social__item" aria-label="Snapgrid"><span class="social__mark"></span>getvelvetmarlow</div>
            <div class="social__item" aria-label="Friendwall"><span class="social__mark"></span>getvelvetmarlow</div>
          </div>
        </div>
      </div>
    </div>
  </div>
</body>
</html>
```